Lorvel MediSpa - Mailchimp Email

I have a list of prospects that I want to email. I'm using Mailchimp. I would like my template to explain that we are now open and ready for business. We are offering 20% off on all services and special procedure combination deals. I want the design to be a template that I can use the same look and feel for future emails - for information giving, beauty tips. monthly promos, etc.

I don't know much about email campaigns, but I'd like to keep it simple, let the people know we're open for business and try to get them to either respond to the email or call for a free consult.
Updates

Thank you all for your hard work on my project.

Target Market(s)

The list criteria is female, income greater than $50,000, between the age of 30 and 65. The area is affluent - Potomac, Bethesda and Chevy Chase Maryland

Industry/Entity Type

Health And Wellness

Font styles to use
Other font styles liked:
• I'd like to keep the font simple like our logo font - again if possible.

Colors

Designer to choose colors to be used in the design.

Requirements
Must have
• my logo, nice pictures related to the medispa business, location "1 block from Brackenridge Harlow Mall', link to our website
Nice to have
• place to input their info to sign up for future emails - i see this on websites. I don't know if they do this for emails. Mailchimp seems to use them.
• Keep the look and feel of our website if that makes sense - www.lorvelmedispa-example.com.
Should not have
• don't be too busy or too long. Keep it simple if possible.

```html
<!DOCTYPE html>
<html lang="en">
<head>
<meta charset="utf-8">
<title>Lorvel MediSpa – Newsletter</title>
<link href="https://fonts.googleapis.com/css2?family=Lato:wght@300;400;700&display=swap" rel="stylesheet">
<style>
  :root {
    --green: #6a9e33;
    --green-light: #7db83e;
    --green-dark: #5a8a2a;
    --yellow: #f3e03a;
    --ink: #3a3a3a;
    --charcoal: #333333;
    --page: #f2f2f0;
    --white: #ffffff;
  }
  * { box-sizing: border-box; margin: 0; padding: 0; }
  html, body { width: 1200px; height: 2854px; overflow: hidden; }
  body { font-family: "Lato", sans-serif; background: var(--page); color: var(--ink); position: relative; }

  .header { position: absolute; left: 0; top: 0; width: 1200px; height: 200px; background: var(--green); }
  .header-brand { position: absolute; left: 0; top: 0; width: 720px; height: 186px; background: var(--white);
    clip-path: polygon(0 0, 100% 0, 92% 100%, 0 100%); }
  .brand { position: absolute; left: 36px; top: 52px; display: flex; align-items: center; gap: 22px; }
  .brand-mark { width: 80px; height: 80px; border-radius: 50%; background: var(--ink); }
  .brand-name { font-size: 62px; font-weight: 700; color: var(--ink); letter-spacing: 1px; }
  .social { position: absolute; right: 30px; top: 38px; display: flex; gap: 14px; }
  .social span { width: 56px; height: 56px; border: 3px solid var(--white); border-radius: 50%; }
  .call { position: absolute; right: 28px; top: 108px; color: var(--white); font-size: 38px; font-weight: 300; }
  .call strong { font-weight: 700; margin-left: 12px; }

  .hero { position: absolute; left: 0; top: 200px; width: 1200px; height: 566px;
    background: linear-gradient(100deg, #e9e8e8 0%, #e6e2e0 40%, #e8c8b4 62%, #d9a98e 82%, #c98d72 100%); }
  .offer { position: absolute; left: 34px; top: 308px; width: 504px; height: 576px; }
  .offer svg { position: absolute; inset: 0; }
  .offer-text { position: absolute; left: 0; top: 140px; width: 504px; text-align: center; color: var(--white);
    font-weight: 700; font-size: 38px; line-height: 48px; text-transform: uppercase; }
  .offer-text .highlight { color: var(--yellow); }

  .intro { position: absolute; left: 60px; top: 934px; width: 1080px; text-align: center; font-size: 28px; line-height: 46px; font-weight: 400; }
  .intro .name { color: var(--green); }
  .rule { position: absolute; left: 535px; top: 1038px; width: 130px; height: 5px; background: var(--green); }
  .goals { position: absolute; left: 40px; top: 1112px; width: 1120px; text-align: center; font-size: 28px; line-height: 46px; }

  .service { position: absolute; width: 362px; height: 350px; border: 5px solid var(--charcoal);
    border-radius: 46px 0 46px 0; overflow: hidden; }
  .service-photo { position: absolute; inset: 0; }
  .service-label { position: absolute; left: 0; right: 0; top: 146px; height: 64px; background: rgba(106,158,51,0.92);
    color: var(--white); font-size: 32px; display: flex; align-items: center; justify-content: center; text-align: center; line-height: 32px; }
  .service-label.two-line { font-size: 28px; top: 140px; height: 76px; line-height: 32px; }

  .newsletter { position: absolute; left: 0; top: 2140px; width: 1200px; height: 366px; background: var(--charcoal); }
  .newsletter-title { position: absolute; left: 0; top: 44px; width: 1200px; text-align: center; color: var(--white); font-size: 46px; font-weight: 400; }
  .email-field { position: absolute; left: 214px; top: 126px; width: 742px; height: 86px; border: 2px solid #9a9a9a; border-radius: 43px;
    display: flex; align-items: center; justify-content: center; gap: 18px; color: var(--white); font-size: 29px; font-weight: 300; }
  .subscribe { position: absolute; left: 374px; top: 230px; width: 422px; height: 86px; background: var(--green); border-radius: 43px;
    color: var(--white); font-size: 34px; display: flex; align-items: center; justify-content: center; }
  .newsletter-mark { position: absolute; right: 40px; top: 200px; width: 150px; height: 150px; border-radius: 50%; background: #3d3d3d; }

  .more-info { position: absolute; left: 0; top: 2506px; width: 1200px; height: 266px; background: var(--white); }
  .more-band { position: absolute; left: 222px; top: 84px; width: 756px; height: 64px; background: var(--green);
    border-radius: 10px 30px 10px 30px; color: var(--white); font-size: 34px; display: flex; align-items: center; justify-content: center; }
  .more-url { position: absolute; left: 0; top: 150px; width: 1200px; text-align: center; color: var(--green); font-size: 54px; font-weight: 400; }

  .footer { position: absolute; left: 0; top: 2772px; width: 1200px; height: 82px; background: var(--green);
    color: var(--white); font-size: 24px; font-weight: 700; display: flex; align-items: center; justify-content: center; }
</style>
</head>
<body>
  <header class="header">
    <div class="header-brand">
      <div class="brand"><span class="brand-mark"></span><span class="brand-name">Lorvel MediSpa</span></div>
    </div>
    <div class="social" aria-label="Social links"><span></span><span></span><span></span></div>
    <div class="call">Call Us:<strong>240.555.0147</strong></div>
  </header>

  <section class="hero" role="img" aria-label="Photo of a woman resting her head on her arm at a spa"></section>

  <div class="offer">
    <svg viewBox="0 0 504 576" width="504" height="576" aria-hidden="true">
      <path d="M14 0 H490 Q504 0 504 14 V424 L252 576 L0 424 V14 Q0 0 14 0 Z" fill="#6a9e33"/>
      <path d="M20 8 H484 Q496 8 496 20 V418 L252 564 L8 418 V20 Q8 8 20 8 Z" fill="#74ad38"/>
      <path d="M28 20 H476 Q484 20 484 28 V410 L252 548 L20 410 V28 Q20 20 28 20 Z" fill="none" stroke="#a6d06f" stroke-width="2"/>
    </svg>
    <div class="offer-text">
      We are offering<br>
      <span class="highlight">20% off on all services</span><br>
      and special procedure<br>
      combination deals
    </div>
  </div>

  <p class="intro"><span class="name">Lorvel MediSpa</span> is now open, 1 block from Brackenridge Harlow Mall. We use technologies and medical science to help our patients achieve natural beauty.</p>
  <div class="rule"></div>
  <p class="goals">Our goals are natural beauty and patient satisfaction. We strive to make sure you are happy with your look. Call us today for a free consultation.</p>

  <div class="service" style="left:32px;top:1290px;">
    <div class="service-photo" role="img" aria-label="Facial aesthetic photo" style="background:linear-gradient(135deg,#2c2c2c,#7a3b30 60%,#b04038);"></div>
    <div class="service-label">Facial Aesthetic</div>
  </div>
  <div class="service" style="left:420px;top:1290px;">
    <div class="service-photo" role="img" aria-label="Laser treatment photo" style="background:linear-gradient(135deg,#6e5a4c,#a98466 55%,#c9a88a);"></div>
    <div class="service-label">Laser Treatments</div>
  </div>
  <div class="service" style="left:804px;top:1290px;">
    <div class="service-photo" role="img" aria-label="Body contouring photo" style="background:linear-gradient(180deg,#d8b8a2,#caa48c 55%,#b8c0c8);"></div>
    <div class="service-label two-line">Body Contouring /<br>Weight Loss</div>
  </div>
  <div class="service" style="left:200px;top:1680px;">
    <div class="service-photo" role="img" aria-label="Skin rejuvenation photo" style="background:linear-gradient(90deg,#d8d8d8,#e6d6cc 50%,#e8cfc0);"></div>
    <div class="service-label">Skin Rejuvenation</div>
  </div>
  <div class="service" style="left:584px;top:1680px;">
    <div class="service-photo" role="img" aria-label="Skin care product bottles" style="background:linear-gradient(180deg,#ffffff,#dfe6f2 50%,#8fa8d8);"></div>
    <div class="service-label">Skin Care Products</div>
  </div>

  <section class="newsletter">
    <h2 class="newsletter-title">Subscribe to Our Newsletter</h2>
    <div class="email-field">
      <svg width="40" height="30" viewBox="0 0 40 30" aria-hidden="true">
        <rect x="0" y="0" width="40" height="30" rx="3" fill="#6a9e33"/>
        <path d="M2 3 L20 17 L38 3" fill="none" stroke="#333333" stroke-width="3"/>
      </svg>
      Enter Your Email Address
    </div>
    <div class="subscribe">SUBSCRIBE</div>
    <div class="newsletter-mark" aria-hidden="true"></div>
  </section>

  <section class="more-info">
    <div class="more-band">For More Information Visit</div>
    <div class="more-url">www.lorvelmedispa-example.com</div>
  </section>

  <footer class="footer">Copyright @ 2019 lorvelmedispa</footer>
</body>
</html>
```